Gestatlung flyer (2 pages) format selectable, based accompanying templates (logo, text) Projektflyer "intercultural cooking class with asylum seekers' data Friday evenings 17. 03 / 24.03 / 31.03 / 07.04 / Time: 18:30 Location: KL Marbeck St. Gallen Title: Intercultural cooking class with asylum seekers text: cooking course is run by asylum seekers. Cooking together, outlandish specialties, exciting conversations Registration: until 24h before the event costs: Expenses participation at its discretion Logos: Pepper Grove, Stifung Valmora. The logos should be listed as the sender and do not dominate the flyer. --------- Just be creative, everything is permitted and desired. The goal is that we make as many people as possible aware of this flyer. The flyers are distributed and the target audience is young adults. Dr Flyer should be correspondingly Modern, Emotianal and sales driven (screaming). Strong Typo, clearly legible and the content clearly structured. The shape of the flyer is free! In total we leave you as much creative freedom as possible. I am looking forward to the many great suggestions and am very excited about the results.

Target Market(s)

Young adults

Font styles to use
Serif
Sans Serif
Script

Requirements
Must have
• Textunterstüzung by appropriate images. Friendly design, bright colors. Very easy to read, weighted Title entsrprechend.
Nice to have
• Emotional Cook image or illustration
Should not have
• No picture with white and dark-skinned people.

```html
<!DOCTYPE html>
<html lang="de">
<head>
<meta charset="utf-8">
<title>Interkultureller Kochkurs – pepper grove</title>
<link rel="stylesheet" href="https://fonts.googleapis.com/css2?family=Bangers&family=Comfortaa:wght@700&family=Alegreya+SC:wght@400;700&display=swap">
<style>
  :root {
    --sun: #f2bf5b;
    --brick: #8a3a1c;
    --brick-edge: #e7a13d;
    --earth: #6e2a14;
    --counter: #e3992f;
    --ink: #5a2410;
    --accent: #f3a43d;
    --white: #ffffff;
    --scene: #c9773a;
  }
  * { margin: 0; padding: 0; box-sizing: border-box; }
  html, body { width: 848px; height: 1200px; overflow: hidden; background: var(--sun); }
  .flyer { position: relative; width: 848px; height: 1200px; background: var(--sun); overflow: hidden; }
  .ground { position: absolute; left: 0; top: 938px; width: 848px; height: 262px; background: var(--earth); }
  .wall { position: absolute; left: 0; top: 0; width: 848px; height: 1200px; }
  .brand {
    position: absolute; top: 48px; left: 0; width: 100%; text-align: center;
    font-family: "Comfortaa", sans-serif; font-weight: 700; font-size: 62px;
    color: var(--earth); letter-spacing: 1px;
  }
  .title {
    position: absolute; top: 282px; left: 0; width: 100%; text-align: center;
    font-family: "Bangers", cursive; color: var(--white); line-height: 1;
    letter-spacing: 2px;
  }
  .title span { display: block; }
  .title .l1 { font-size: 66px; }
  .title .l2 { font-size: 58px; margin-top: 4px; }
  .title .l3 { font-size: 50px; margin-top: 8px; }
  .intro {
    position: absolute; top: 484px; left: 0; width: 100%; text-align: center;
    font-family: "Alegreya SC", serif; font-size: 21px; line-height: 35px;
    color: var(--accent); letter-spacing: 0.5px;
  }
  .kitchen {
    position: absolute; left: 64px; top: 594px; width: 763px; height: 250px;
    background: linear-gradient(180deg, var(--scene) 0%, #e6e2dc 78%, #ffffff 100%);
    border-radius: 6px;
  }
  .details {
    position: absolute; left: 134px; top: 840px; width: 582px; height: 360px;
    background: var(--counter); padding: 32px 44px 0;
    font-family: "Alegreya SC", serif; color: var(--ink);
  }
  .row { border-bottom: 1.5px solid var(--ink); padding: 0 0 8px; margin-bottom: 12px; }
  .label { font-weight: 700; font-size: 19px; letter-spacing: 0.5px; }
  .value { font-size: 18px; letter-spacing: 0.3px; margin-top: 2px; }
  .split { display: flex; border-bottom: none; }
  .split .cell { flex: 1; }
  .split .cell + .cell { border-left: 1.5px solid var(--ink); padding-left: 40px; flex: 0 0 170px; }
</style>
</head>
<body>
<div class="flyer">
  <div class="ground"></div>
  <svg class="wall" viewBox="0 0 848 1200" role="img" aria-label="Gemauerte Backsteinwand als Hintergrund">
    <path fill="var(--brick-edge)" d="M60 230 L150 200 L160 170 L310 160 L330 140 L470 150 L520 170 L640 165 L700 195 L760 200 L790 260 L770 330 L800 400 L780 480 L810 560 L790 640 L810 700 L760 760 L90 760 L40 700 L30 600 L55 520 L25 440 L50 360 L20 300 Z"/>
    <path fill="var(--brick)" d="M80 240 L165 215 L175 185 L315 176 L335 158 L465 166 L515 186 L635 180 L690 208 L748 214 L772 265 L752 330 L782 402 L762 480 L792 560 L772 640 L790 700 L745 750 L100 750 L58 696 L48 600 L72 520 L44 440 L68 362 L40 304 Z"/>
  </svg>
  <div class="brand">pepper grove</div>
  <h1 class="title">
    <span class="l1">Interkultureller</span>
    <span class="l2">Kochkurs</span>
    <span class="l3">mit Asylsuchenden</span>
  </h1>
  <p class="intro">Kochkurs wird von Asylsuchenden geleitet.<br>Gemeinsames Kochen, fremdländische Spezial-<br>itäten, spannende Gespräche</p>
  <div class="kitchen" role="img" aria-label="Illustration: Gruppe kocht gemeinsam an einer Küchentheke mit Koch in der Mitte"></div>
  <section class="details">
    <div class="row"><div class="label">Kosten</div><div class="value">Unkostenbeteiligung nach eigenem Ermessen</div></div>
    <div class="row"><div class="label">Anmeldung</div><div class="value">bis 24h vor dem Anlass</div></div>
    <div class="row"><div class="label">Daten</div><div class="value">Freitag Abende 17. 03 / 24.03 / 31.03 / 07.04/</div></div>
    <div class="row split">
      <div class="cell"><div class="label">Ort</div><div class="value">KL Marbeck St.Gallen</div></div>
      <div class="cell"><div class="label">Zeit</div><div class="value">18.30h</div></div>
    </div>
  </section>
</div>
</body>
</html>
```